Corvane Electrical Solutions

On one side. LOGO (underneath:) Commercial Industrial Residential

- NAME & CONTACT DETAILS

Marcus T. Hollings
Project Manager

(Cell icon) (441) 582-6197
(Email icon) cvnelectricalsoultions@mailventra.com
(Facebook & Instagram icons )@cvnelectricalsolutions

Other side: LOGO - underneath ELECTRICAL CONSTRUCTION & MAINTENANCE . LED LIGHTING & AUTOMATION . LIFE SAFETY SYSTEMS (FIRE ALARM / SECURITY) . DATA & COMMUNICATION

```html
<!DOCTYPE html>
<html lang="en">
<head>
<meta charset="UTF-8">
<title>Corvane Electrical Solutions – Business Card</title>
<link href="https://fonts.googleapis.com/css2?family=Open+Sans:wght@400;600;700&display=swap" rel="stylesheet">
<style>
  :root {
    --teal: #1b5b73;
    --grey: #4f5254;
    --soft-grey: #7a7d80;
    --card: #ffffff;
    --backdrop: #e6e7e8;
  }
  * { margin: 0; padding: 0; box-sizing: border-box; }
  html, body {
    width: 1200px; height: 900px; overflow: hidden;
    background: var(--backdrop);
    font-family: "Open Sans", Arial, sans-serif;
  }
  .sheet {
    width: 1200px; height: 900px;
    display: flex; flex-direction: column;
    align-items: center; justify-content: center; gap: 34px;
  }
  .card {
    position: relative;
    width: 700px; height: 400px;
    background: var(--card);
    box-shadow: 0 4px 14px rgba(0,0,0,0.12);
  }

  /* Contact side */
  .accent-bar {
    position: absolute; left: 0; width: 8px; background: var(--teal);
  }
  .accent-bar.top { top: 44px; height: 44px; }
  .accent-bar.bottom { top: 296px; height: 50px; }
  .holder { position: absolute; left: 32px; top: 40px; }
  .holder-name { color: var(--teal); font-weight: 700; font-size: 20px; }
  .holder-role { color: var(--soft-grey); font-size: 11px; margin-top: 1px; }
  .brand-block {
    position: absolute; left: 0; right: 0; top: 150px; text-align: center;
  }
  .brand-name {
    color: var(--teal); font-weight: 700; font-size: 30px; letter-spacing: 0.5px;
  }
  .brand-sectors {
    color: var(--grey); font-weight: 600; font-size: 15px; margin-top: 8px; letter-spacing: 0.3px;
  }
  .contact-list { position: absolute; left: 32px; top: 296px; list-style: none; }
  .contact-item {
    display: flex; align-items: center; gap: 12px;
    color: var(--grey); font-size: 15px; height: 26px;
  }
  .contact-icon { width: 18px; height: 18px; flex: none; }

  /* Services side */
  .card.services .brand-block { top: 70px; }
  .card.services .brand-name { font-size: 38px; }
  .service-list {
    position: absolute; left: 0; right: 0; top: 160px;
    list-style: none; text-align: center;
    color: var(--teal); font-size: 15px; line-height: 24px; text-transform: uppercase;
  }
  .service-list li::before { content: "• "; }
  .social-row {
    position: absolute; left: 0; right: 0; top: 300px;
    display: flex; justify-content: center; align-items: center; gap: 10px;
  }
  .social-rule { width: 74px; height: 3px; background: var(--teal); }
  .social-dot { width: 30px; height: 30px; border-radius: 50%; background: var(--teal); }
  .social-handle {
    position: absolute; left: 0; right: 0; top: 340px; text-align: center;
    color: var(--teal); font-size: 13px;
  }
</style>
</head>
<body>
<main class="sheet">

  <section class="card contact-side">
    <span class="accent-bar top"></span>
    <span class="accent-bar bottom"></span>
    <div class="holder">
      <p class="holder-name">Marcus T. Hollings</p>
      <p class="holder-role">Project Manager</p>
    </div>
    <div class="brand-block">
      <p class="brand-name">Corvane Electrical Solutions</p>
      <p class="brand-sectors">Commercial Industrial Residential</p>
    </div>
    <ul class="contact-list">
      <li class="contact-item">
        <svg class="contact-icon" viewBox="0 0 18 18" aria-hidden="true">
          <rect x="5" y="1.5" width="8" height="15" rx="1.5" fill="none" stroke="#4f5254" stroke-width="1.4"/>
          <line x1="8" y1="14" x2="10" y2="14" stroke="#4f5254" stroke-width="1.4"/>
        </svg>
        (441) 582-6197
      </li>
      <li class="contact-item">
        <svg class="contact-icon" viewBox="0 0 18 18" aria-hidden="true">
          <rect x="1.5" y="4" width="15" height="10" fill="none" stroke="#4f5254" stroke-width="1.4"/>
          <polyline points="1.5,4 9,10 16.5,4" fill="none" stroke="#4f5254" stroke-width="1.4"/>
        </svg>
        cvnelectricalsoultions@mailventra.com
      </li>
    </ul>
  </section>

  <section class="card services">
    <div class="brand-block">
      <p class="brand-name">Corvane Electrical Solutions</p>
    </div>
    <ul class="service-list">
      <li>Electrical Construction &amp; Maintenance</li>
      <li>Life Safety Systems (Fire Alarm / Security)</li>
      <li>LED Lighting &amp; Automation</li>
      <li>Data &amp; Communication</li>
    </ul>
    <div class="social-row">
      <span class="social-rule"></span>
      <span class="social-dot"></span>
      <span class="social-dot"></span>
      <span class="social-rule"></span>
    </div>
    <p class="social-handle">@cvnelectricalsolutions</p>
  </section>

</main>
</body>
</html>
```